Website Landing Page for Marlowe Systems

Create a custom designed website landing page for our business. Looking for a professional upscale design that incorporates our logo and logo colors into the theme. I want a standard fixed frame website, not a constant scrolling format that seems to be the trend. To start with I'm looking for more of the graphic design part, maybe a concept or theme, I don't expect to see a finished project. Not interested in generic templates or layouts.

The name of our company is Marlowe Systems and I've attached our logo below. I'd like to have the web page have the same look and feel of our logo, as well as the colors. Our company, Marlowe Systems does system design, installation, and programming, of residential and commercial Audio/Video and Automation systems. We do home theaters, lighting and building automation, video conferencing systems, security camera installations, conference rooms, projectors, distributed audio systems, and similar Technology projects. This will be a professional services/informational website. We will not sell products on this website. This website will be used to advertise our company and communicate our services to prospective customers. Having a well designed, professional and clean website is one way we want to distinguish our company from the competition.

Here are some examples of what I consider a professional well designed website
http://www.qrzstudio.example/Work/

Last year we had our tradeloft store designed (with PixelHarbor) and I'm really happy with the way it turned out. You can see it at www.KelpGearDepot.example I consider this to be a great design and looking for the same level of quality with this new website. However, do not copy or use any part of this design in this new project. This tradeloft store is completely separate from our other company Marlowe Systems. I only mention this tradeloft store an an example of good work.

Target Market(s)

People interested in Audio/Video, home theaters, home automation. We do sales, system design, and programming. We typically work on larger projects with both residential and commercial customers.

Industry/Entity Type

Business

Number of Pages Required

1 page

Requirements
Must have
• Great design elements. Please use a white background. I think white goes well with our logo colors.

```html
<!DOCTYPE html>
<html lang="en">
<head>
<meta charset="utf-8">
<title>Marlowe Systems</title>
<link href="https://fonts.googleapis.com/css2?family=Oswald:wght@500;600&family=Teko:wght@400;500&family=Source+Sans+3:wght@400;600&display=swap" rel="stylesheet">
<style>
:root{
  --blue:#2b6cb4;
  --green:#3caa3a;
  --ink:#3c3f44;
  --muted:#8a8f95;
  --bg:#f3f4f6;
  --tile-grey:#c8d1db;
  --tile-green:#cbe8bc;
  --rule:#dcdfe3;
  --fog:#e6eaee;
  --sky:#b9c3cc;
}
*{margin:0;padding:0;box-sizing:border-box}
html,body{width:1200px;height:900px;overflow:hidden}
body{background:var(--bg);font-family:"Source Sans 3",Arial,sans-serif;color:var(--ink);position:relative}
.abs{position:absolute}

/* skyline backdrop */
.skyline{left:0;top:560px;width:1200px;height:230px;
  background:linear-gradient(180deg,rgba(243,244,246,0) 0%,var(--sky) 45%,var(--fog) 75%,rgba(243,244,246,0) 100%);opacity:.7}

/* service tiles */
.tile{top:55px;height:144px;width:164px;padding:22px 0 0 17px;overflow:hidden}
.tile--grey{background:linear-gradient(135deg,#d3dae2,var(--tile-grey))}
.tile--green{background:linear-gradient(135deg,#d8efcc,var(--tile-green))}
.tile__icon{width:34px;height:34px;display:block;margin-bottom:6px}
.tile__title{font-family:"Oswald",sans-serif;font-weight:500;font-size:18px;letter-spacing:-.2px;color:#1e2226;line-height:1.1;margin-top:2px}
.tile__text{font-size:9.5px;color:#555b62;margin-top:6px}

/* brand */
.brand{left:520px;top:12px;width:160px;text-align:center}
.brand__mark{width:64px;height:64px;border-radius:50%;border:5px solid var(--blue);margin:0 auto 6px}
.brand__name{font-family:"Teko",sans-serif;font-weight:500;font-size:25px;line-height:.9;color:var(--blue);letter-spacing:1px}
.brand__rule{height:1px;background:var(--rule);margin:14px 0 12px}
.social{display:flex;gap:6px;justify-content:center}
.social span{width:14px;height:14px;border-radius:2px;background:#9aa0a6}

/* services */
.services__ring{left:232px;top:228px;width:84px;height:84px;border-radius:50%;border:4px solid #dde4ec}
.services__title{left:252px;top:243px;font-family:"Teko",sans-serif;font-weight:400;font-size:50px;letter-spacing:3px;color:var(--blue);line-height:1}
.services__list{left:252px;top:326px;list-style:none}
.services__list li{font-size:11.5px;height:30.1px;color:var(--ink)}
.services__list li.is-active{color:var(--green)}
.services__list li.is-active span{border-bottom:1px solid var(--green);padding-bottom:3px}

/* feature */
.feature__photo{left:615px;top:245px;width:338px;height:240px;border:6px solid #c5c8cc;
  background:linear-gradient(180deg,#f2f2f2 0%,#8b5c44 30%,#7a5240 55%,#5a5d62 78%,#cfd2d6 100%)}
.feature__title{left:738px;top:447px;font-family:"Teko",sans-serif;font-weight:500;line-height:.82;letter-spacing:2px}
.feature__title .a{font-size:42px;color:#fff;display:block}
.feature__title .b{font-size:46px;color:var(--green);display:block}
.feature__text{left:620px;top:538px;width:254px;text-align:right;font-size:10.5px;line-height:13.3px;color:var(--muted)}
.feature__more{left:886px;top:535px;width:64px;height:64px;border-radius:50%;border:4px solid var(--green);
  display:flex;align-items:center;justify-content:center;font-family:"Teko",sans-serif;font-size:21px;letter-spacing:2px;color:var(--green);background:#fff}

/* footer */
.foot__head{top:692px;font-size:11.5px;font-weight:600;letter-spacing:1.5px;color:#222}
.foot__text{top:722px;font-size:8.5px;line-height:13.2px;color:var(--muted);width:200px}
.foot__mark{left:548px;top:698px;width:104px;height:104px;border-radius:50%;border:7px solid #c9cacc}
.foot__social{left:249px;top:802px;display:flex;gap:8px}
.foot__social span{width:11px;height:11px;border-radius:2px;background:#a3a8ad}
.foot__rule{left:248px;top:843px;width:703px;height:1px;background:var(--rule)}
.foot__copy{left:0;top:864px;width:1200px;text-align:center;font-size:8.5px;color:var(--muted)}
</style>
</head>
<body>

<div class="abs skyline" role="img" aria-label="Misty city skyline with towers and cranes"></div>

<!-- left tiles -->
<div class="abs tile tile--grey" style="left:0" role="img" aria-label="Faded office interior photo">
  <svg class="tile__icon" viewBox="0 0 34 34" fill="none" stroke="#1e2226" stroke-width="1.6"><path d="M7 3c-2 2 2 3 0 5M13 3c-2 2 2 3 0 5M19 3c-2 2 2 3 0 5"/><path d="M4 13h20a3 3 0 0 1 0 6H6a3 3 0 0 0 0 6h20" stroke-dasharray="3 2"/><path d="M4 30h16"/></svg>
  <div class="tile__title">AUTOMATION SYSTEMS</div>
  <div class="tile__text">Lorem ipsum dolor sit amet</div>
</div>
<div class="abs tile tile--green" style="left:167px" role="img" aria-label="Faded city view photo">
  <svg class="tile__icon" viewBox="0 0 34 34" fill="none" stroke="#1e2226" stroke-width="1.8"><rect x="2" y="4" width="30" height="20" rx="1"/><path d="M2 19h30M13 24l-2 6h12l-2-6M9 30h16M14 14l5-5M17 14l2-2"/></svg>
  <div class="tile__title">SYSTEM DESIGN</div>
  <div class="tile__text">Lorem ipsum dolor sit amet</div>
</div>
<div class="abs tile tile--grey" style="left:334px" role="img" aria-label="Faded living room photo">
  <svg class="tile__icon" viewBox="0 0 34 34" fill="none" stroke="#1e2226"><circle cx="17" cy="14" r="8" stroke-width="5" stroke-dasharray="3.2 1.6"/><circle cx="17" cy="14" r="3" stroke-width="2"/><path d="M4 24v6h26v-6" stroke-width="2"/></svg>
  <div class="tile__title">INSTALLATION</div>
  <div class="tile__text">Lorem ipsum dolor sit amet</div>
</div>

<!-- brand -->
<div class="abs brand">
  <div class="brand__mark"></div>
  <div class="brand__name">MARLOWE<br>SYSTEMS</div>
  <div class="brand__rule"></div>
  <div class="social"><span></span><span></span><span></span><span></span></div>
</div>

<!-- right tiles -->
<div class="abs tile tile--green" style="left:702px" role="img" aria-label="Faded lounge photo">
  <svg class="tile__icon" viewBox="0 0 34 34" fill="none" stroke="#1e2226" stroke-width="1.8"><circle cx="17" cy="17" r="15"/><path d="M13 10l10 7-10 7z"/></svg>
  <div class="tile__title">AUDIO/VIDEO</div>
  <div class="tile__text">Lorem ipsum dolor sit amet</div>
</div>
<div class="abs tile tile--grey" style="left:870px" role="img" aria-label="Faded office interior photo">
  <svg class="tile__icon" viewBox="0 0 34 34" fill="none" stroke="#1e2226" stroke-width="1.6"><path d="M7 3c-2 2 2 3 0 5M13 3c-2 2 2 3 0 5M19 3c-2 2 2 3 0 5"/><path d="M4 13h20a3 3 0 0 1 0 6H6a3 3 0 0 0 0 6h20" stroke-dasharray="3 2"/><path d="M4 30h16"/></svg>
  <div class="tile__title">AUTOMATION SYSTEMS</div>
  <div class="tile__text">Lorem ipsum dolor sit amet</div>
</div>
<div class="abs tile tile--green" style="left:1036px" role="img" aria-label="Faded modern building photo">
  <svg class="tile__icon" viewBox="0 0 34 34" fill="none" stroke="#1e2226" stroke-width="2.2"><path d="M10 9l-8 8 8 8M24 9l8 8-8 8M20 5l-6 24"/></svg>
  <div class="tile__title">PROGRAMMING</div>
  <div class="tile__text">Lorem ipsum dolor sit amet</div>
</div>

<!-- services -->
<div class="abs services__ring"></div>
<h1 class="abs services__title">OUR SERVICES</h1>
<ul class="abs services__list">
  <li class="is-active"><span>01. HOME THEATERS</span></li>
  <li>02. LIGHTING AND BUILDING AUTOMATION</li>
  <li>03. VIDEO CONFERENCING SYSTEMS</li>
  <li>04. SECURITY CAMERA INSTALLATIONS</li>
  <li>05. CONFERENCE ROOMS</li>
  <li>06. PROJECTORS</li>
  <li>07. DISTRIBUTED AUDIO SYSTEMS</li>
  <li>08. TECHNOLOGY PROJECTS</li>
</ul>

<!-- feature -->
<div class="abs feature__photo" role="img" aria-label="Conference room with long table, chairs and wall screen"></div>
<h2 class="abs feature__title"><span class="a">HOME</span><span class="b">THEATERS</span></h2>
<p class="abs feature__text">Lorem ipsum dolor sit amet, consectetur adipiscing elit, sed do eiusmod tempor incididunt ut labore et dolore magna aliqua. Ut enim ad minim veniam, quis nostrud exercitation ullamco laboris nisi</p>
<div class="abs feature__more">MORE</div>

<!-- footer -->
<h3 class="abs foot__head" style="left:250px">CONTACT US</h3>
<p class="abs foot__text" style="left:248px">Lorem Ipsum is simply dummy text of the printing and typesetting industry. Lorem Ipsum has been the industry's standard dummy text ever since the 1500s, when an unknown printer took a galley of type and</p>
<div class="abs foot__social"><span></span><span></span><span></span><span></span></div>

<div class="abs foot__mark"></div>

<h3 class="abs foot__head" style="left:850px;width:100px;text-align:right">ABOUT US</h3>
<p class="abs foot__text" style="left:740px;width:210px;text-align:right">Lorem Ipsum is simply dummy text of the printing and typesetting industry. Lorem Ipsum has been the industry's standard dummy text ever since the 1500s, when an unknown printer took a galley of type and scrambled it to make a type specimen book.</p>

<div class="abs foot__rule"></div>
<p class="abs foot__copy">© 2017, Marlowe Systems</p>

</body>
</html>
```